DAWL Tea & Herbal Tea Packaging Labels

We are seeking new consistent front label designs that we can use for both retail and wholesale packaging purposes:

DAWL PHILOSOPHY

DAWL provides a selection of ‘energy enhanced’ signature infusion blends that taste great while assisting a person deeply on several levels – emotional, mental, physical and spiritual.

We source quality ingredients and specifically use certified organic, spray free and wildcrafted ingredients for our herbal blends.

DAWL’s PRODUCT RANGE

A. 6 standard signature herbal blends (standard range)
B. 2 seasonal blends - which change every quarter (1 x herbal blend, 1 x tea-based blend)
C. selection of teas – black, green, white, oolong (which vary in type and number)
D. custom and limited edition blends – herbal and teas
E. tea drinking accessories.

11 LABELS ARE REQUIRED

Labels 1-8 for Herbal Blends (to be denoted by an accent of SILVER)
Labels 9-10 for Teas (to be denoted by an accent of GOLD)
Label 11 for Accessories

LABEL SIZE

Current front label dimensions: 63.5 x 72mm long – willing to look at alternate label size
Current ‘usable area’ of smallest resealable bag: 110 x 130mm long

** PLEASE SEE ATTACHED WORD DOC FOR COMPLETE SPECIFICATION - PLEASE READ BEFORE COMMENCING ANY WORK **
Updates

hi,

forgot to include an attachment of the current labels for herbal teas that are used... here is a link to the PDF.

http://files.quorvane.example/u/47381652/DAWL-Herbal-Labels.pdf

thanks Malcolm

Hi,

please note we have attached a jpg of the packaging the label goes onto... it is in the attached files in the brief - called packaging.

thanks Malcolm

Hi, we've uploaded some pics of the current packaging to give you a sense of the packaging we are using and the space on the front pack to work with.

many thanks.

Target Market(s)

Women and men aged 30-55 with an interest in natural products, emotional/spiritual wellbeing and support.

DAWL DISTRIBUTION

Online store for retail sales,
Cafes for food service,
Practitioner (naturopaths, massage therapists, energy healers) clinics and stores.

Industry/Entity Type

Retail

Requirements
Must have
• Each label should have:
• Current logo and tagline;
• Website name;
• Silver accent for herbal range labels;
• Gold accent for tea range labels;
• Colour-coding for the 6 signature herbals.
• ** PLEASE SEE ATTACHED WORD DOC FOR COMPLETE SPECIFICATION - PLEASE READ BEFORE COMMENCING ANY WORK **
Nice to have
• Mrs Eaves font for text (to match logo font type)

```html
<!DOCTYPE html>
<html lang="en">
<head>
<meta charset="utf-8">
<title>DAWL infusions – Rooibos Lemon labels</title>
<link rel="stylesheet" href="https://fonts.googleapis.com/css2?family=Sorts+Mill+Goudy:ital@0;1&display=swap">
<style>
  :root {
    --teal: #23a78b;
    --ink: #231f20;
    --pink: #e8308a;
    --silver-light: #f2f2f2;
    --silver-mid: #c9c9c9;
    --silver-dark: #9a9a9a;
    --paper: #ffffff;
  }
  * { box-sizing: border-box; margin: 0; padding: 0; }
  html, body {
    width: 1200px; height: 900px; overflow: hidden;
    background: var(--paper);
    font-family: "Sorts Mill Goudy", "Georgia", serif;
    color: var(--ink);
  }
  .canvas { position: relative; width: 1200px; height: 900px; }

  .label {
    position: absolute; top: 30px; width: 522px; height: 851px;
    border: 4px solid var(--teal);
    background: linear-gradient(135deg, var(--silver-mid) 0%, var(--silver-light) 30%, var(--silver-mid) 60%, var(--silver-dark) 100%);
  }
  .label--first { left: 70px; }
  .label--second { left: 619px; }

  .label__panel {
    position: absolute; left: 13px; top: 11px; width: 490px; height: 819px;
    background: var(--paper);
    border: 2px solid var(--teal);
    text-align: center;
  }
  .label__panel > * { position: absolute; left: 0; right: 0; }

  .brand {
    top: 60px; display: flex; justify-content: center; align-items: baseline; gap: 10px;
    color: var(--ink); font-weight: 400;
  }
  .brand__name { font-size: 66px; letter-spacing: 1px; line-height: 1; }
  .brand__range { font-size: 30px; line-height: 1; }
  .brand__dot {
    width: 30px; height: 30px; border-radius: 50%; background: var(--pink);
    align-self: center; margin: 0 -2px;
  }

  .blend-art {
    top: 152px; margin: 0 auto; background: var(--teal);
  }
  .blend-art--grass { width: 100px; height: 130px; border-radius: 80% 10% 60% 20%; left: 190px; right: auto; }
  .blend-art--rose { width: 150px; height: 128px; border-radius: 45%; left: 167px; right: auto; }

  .blend-name { top: 290px; font-size: 71px; line-height: 1; white-space: nowrap; }
  .blend-benefit { top: 394px; font-size: 25px; color: var(--teal); line-height: 1; }
  .blend-sourcing { top: 440px; font-size: 17.5px; line-height: 1; }

  .blend-story, .serving {
    left: 106px; right: 107px; font-size: 14.4px; line-height: 20px;
    text-align: justify; text-align-last: center; letter-spacing: 0.3px;
  }
  .blend-story { top: 480px; }
  .serving { top: 677px; text-align-last: left; }

  .cup-line {
    top: 609px; display: flex; justify-content: center; align-items: flex-end; gap: 4px;
    color: var(--pink); font-style: italic; font-size: 17px;
  }
  .cup-line__art { width: 56px; height: 48px; border-radius: 40% 40% 50% 50%; background: #f7b9d6; }

  .website { top: 780px; font-size: 24px; color: var(--teal); letter-spacing: 1px; }
</style>
</head>
<body>
<main class="canvas">

  <article class="label label--first">
    <div class="label__panel">
      <header class="brand">
        <span class="brand__name">DAWL</span>
        <span class="brand__dot" aria-hidden="true"></span>
        <span class="brand__range">infusions</span>
      </header>
      <div class="blend-art blend-art--grass" role="img" aria-label="Teal illustration of sweeping rooibos grass"></div>
      <h1 class="blend-name">Rooibos Lemon</h1>
      <p class="blend-benefit">Centres and grounds your energy</p>
      <p class="blend-sourcing">Certified Organic and Wildcrafted Ingredients</p>
      <p class="blend-story">Soothing rose brings a lovely balance to the trinity of light, refreshing lemon flavours and the earthy anti-oxidant packed rooibos. Reconnecting you to your internal base, this blend imbues the feeling of being ‘at home.’</p>
      <div class="cup-line">
        <span>love in every cup</span>
        <span class="cup-line__art" role="img" aria-label="Pink line drawing of a teacup with flowers"></span>
      </div>
      <p class="serving">Serving: For Optimum flavour pour freshly boiled water over one generous teaspoon per cup and steep 3-5 minutes.</p>
      <p class="website">www.dawl.example</p>
    </div>
  </article>

  <article class="label label--second">
    <div class="label__panel">
      <header class="brand">
        <span class="brand__name">DAWL</span>
        <span class="brand__dot" aria-hidden="true"></span>
        <span class="brand__range">infusions</span>
      </header>
      <div class="blend-art blend-art--rose" role="img" aria-label="Teal illustration of an open rose"></div>
      <h2 class="blend-name">Rooibos Lemon</h2>
      <p class="blend-benefit">Centres and grounds your energy</p>
      <p class="blend-sourcing">Certified Organic and Wildcrafted Ingredients</p>
      <p class="blend-story">Soothing rose brings a lovely balance to the trinity of light, refreshing lemon flavours and the earthy anti-oxidant packed rooibos. Reconnecting you to your internal base, this blend imbues the feeling of being ‘at home.’</p>
      <div class="cup-line">
        <span>love in every cup</span>
        <span class="cup-line__art" role="img" aria-label="Pink line drawing of a teacup with flowers"></span>
      </div>
      <p class="serving">Serving: For Optimum flavour pour freshly boiled water over one generous teaspoon per cup and steep 3-5 minutes.</p>
      <p class="website">www.dawl.example</p>
    </div>
  </article>

</main>
</body>
</html>
```